8.5 x 8.5 Dale Morven Flyer

Wednesday Workouts
with
Dale Morven
@liftwithdalemorven
Sponsored by BRAMBLE CREST HOMES GROUP
Join us Virtually each Wednesday from 7 - 7:30 pm
email frontdesk@bramblecresthomes.example for Vidora Link
reserved for BCHG Agents and Special Invitees
BRAMBLE CREST HOMES
Phone (555) 618-2739

```html
<!DOCTYPE html>
<html lang="en">
<head>
<meta charset="utf-8">
<title>Wednesday Workouts with Dale Morven</title>
<link href="https://fonts.googleapis.com/css2?family=Montserrat:wght@300;500;600;700;800&display=swap" rel="stylesheet">
<style>
  :root {
    --teal: #16819c;
    --teal-glass: rgba(40, 160, 190, 0.55);
    --white: #ffffff;
    --stage: #e6e9eb;
    --photo-dark: #2a2c33;
    --photo-mid: #6b6f78;
    --photo-light: #b9c2cc;
  }
  * { margin: 0; padding: 0; box-sizing: border-box; }
  html, body { width: 1200px; height: 675px; overflow: hidden; }
  body { background: var(--stage); font-family: "Montserrat", sans-serif; position: relative; }

  .flyer {
    position: absolute; left: 290px; top: 27px;
    width: 620px; height: 620px; overflow: hidden;
    background: var(--teal);
    box-shadow: 0 6px 24px rgba(0,0,0,0.18);
  }
  .flyer-art { position: absolute; inset: 0; }

  .headline { position: absolute; left: 36px; top: 256px; color: var(--white); line-height: 1; }
  .headline-day { font-weight: 800; font-size: 31px; display: block; }
  .headline-main { font-weight: 800; font-size: 50px; display: block; margin-top: 2px; letter-spacing: -0.5px; }
  .headline-host { font-weight: 300; font-size: 40px; display: block; margin-top: 4px; }
  .headline-host .with { font-size: 24px; margin-right: 6px; }

  .handle {
    position: absolute; left: 104px; top: 402px;
    color: var(--teal); font-weight: 500; font-size: 13px; letter-spacing: 3.5px;
  }

  .join {
    position: absolute; left: 36px; top: 440px;
    color: var(--teal); font-weight: 700; font-size: 13px; line-height: 1.35;
  }
  .join .email { font-weight: 600; font-size: 12px; }

  .sponsor { position: absolute; left: 312px; top: 492px; width: 290px; color: var(--white); }
  .sponsor-note { font-size: 11px; font-weight: 500; padding-bottom: 4px; border-bottom: 1.5px solid var(--white); }
  .sponsor-by { font-size: 12px; font-weight: 500; margin-top: 6px; }
  .sponsor-by strong { font-weight: 700; }
  .sponsor-phone { font-size: 26px; font-weight: 700; margin-top: 4px; letter-spacing: 0.3px; }

  .brand {
    position: absolute; left: 36px; top: 500px;
    display: flex; flex-direction: column; align-items: center; gap: 8px;
  }
  .brand-square { width: 48px; height: 48px; background: var(--white); }
  .brand-name { color: var(--white); font-weight: 700; font-size: 13px; letter-spacing: 0.5px; white-space: nowrap; }
</style>
</head>
<body>
  <article class="flyer">
    <svg class="flyer-art" width="620" height="620" viewBox="0 0 620 620">
      <defs>
        <linearGradient id="photoTone" x1="0" y1="0" x2="1" y2="1">
          <stop offset="0" stop-color="var(--photo-light)"/>
          <stop offset="0.45" stop-color="var(--photo-mid)"/>
          <stop offset="1" stop-color="var(--photo-dark)"/>
        </linearGradient>
      </defs>
      <rect class="photo" role="img" aria-label="Photo of the trainer seated at gym equipment" x="0" y="0" width="620" height="470" fill="url(#photoTone)"/>
      <g class="glass-stripes">
        <polygon points="0,70 260,40 330,52 0,110" fill="var(--teal-glass)"/>
        <polygon points="40,150 420,120 470,138 60,176" fill="var(--teal-glass)"/>
        <polygon points="420,300 620,270 620,300 460,320" fill="var(--teal-glass)"/>
      </g>
      <polygon class="panel" points="0,190 620,420 620,620 0,620" fill="var(--teal)"/>
      <polygon class="handle-band" points="96,396 400,396 388,422 84,422" fill="var(--white)"/>
      <polygon class="join-band" points="0,434 560,434 540,478 0,478" fill="var(--white)"/>
    </svg>

    <h1 class="headline">
      <span class="headline-day">Wednesday</span>
      <span class="headline-main">Workouts</span>
      <span class="headline-host"><span class="with">with</span>Dale Morven</span>
    </h1>

    <p class="handle">@liftwithdalemorven</p>

    <p class="join">Join us Virtually each Wednesday from 7 - 7:30 pm<br>
      <span class="email">email frontdesk@bramblecresthomes.example for Vidora Link</span></p>

    <div class="brand">
      <span class="brand-square"></span>
      <span class="brand-name">BRAMBLE CREST HOMES</span>
    </div>

    <div class="sponsor">
      <p class="sponsor-note">reserved for BCHG Agents and Special Invitees</p>
      <p class="sponsor-by">Sponsored by: <strong>BRAMBLE CREST HOMES</strong></p>
      <p class="sponsor-phone">Ph: (555) 618-2739</p>
    </div>
  </article>
</body>
</html>
```